Law Firm Needs a new Website Design

We need a new website design for our law firm located in Manhattan (Law Offices of Tobias R. Venkland, PLLC).
We have an existing logo that we will to continue using, which can be found in www.VenklandLaw.example.
The Prime Counsel, Top Advocates Logo should also be reflected near the bottom of the Home page.
The website will be 6 pages.

Deliverables:
I want a
1) home page,
2) About Us/Practice Areas page,
3) attorneys,
4) News and Articles page, and
5) Contact and Directions/Privacy Policy page.

The colors of my logo should be in the website.
I also like a touch of black and red.

The website should project "excellence."
We seek to provide the highest quality legal services.
We handle estate planning, wills, trusts, planning for people with disabilities, asset protection and preservation, Medicaid planning, hospital safe discharge, nursing home placement, powers of attorney, health care proxies, living wills, guardianships, probate, estate administration and related litigation.

I would like the colors of my Logo used (including shading where appropriate).
I also want some black on the borders and/or bottom and some red touches throughout the page.

My Logo should appear everywhere that "Law Offices Of Tobias R. Venkland, PLLC" appears.
I want the badges for Prime counsel, Top Advocates, Top Legal Practices, and ZELQ on the Home page.
I do not want too much text on the home page.

We would also like the website to have coding.
The final design should also communicate quality, expertise and stability.
Great start so far by the people who submitted designs.
Thank you.

Industry/Entity Type

Law Firm

Coding

Coded - Design and coding required

Number of Pages Required

5+ page

Colors
3276b5
ec1f27
474747

Requirements
Must have
• Please use my logo each time you mention Law Offices of Tobias R. Venkland, PLLC. Please include the Primecounsel, Top Advocates, Top Legal Practices and Zelq rating Badges on the web home page. I only wish to be contacted by phone. I am not including testimonials and am only using the New York City address.
Nice to have
• Prefer illustrations to photos regarding practice areas
Should not have
• Testimonials, contact me by email, free consultation.

```html
<!DOCTYPE html>
<html lang="en">
<head>
<meta charset="utf-8">
<title>Law Offices of Tobias R. Venkland, PLLC</title>
<link href="https://fonts.googleapis.com/css2?family=Cinzel:wght@400;600&family=Lato:wght@400;700&display=swap" rel="stylesheet">
<style>
:root{
  --blue:#3b82c4;
  --blue-dark:#1f4f86;
  --black:#000;
  --ink:#1c1c1c;
  --grey:#474747;
  --grey-mid:#555;
  --grey-light:#f1f1f1;
  --line:#d6d6d6;
  --white:#fff;
}
*{box-sizing:border-box;margin:0;padding:0}
html,body{width:1200px;height:3220px;overflow:hidden}
body{position:relative;font-family:'Lato',sans-serif;color:var(--ink);background:var(--white)}
.abs{position:absolute}

/* top bar */
.topbar{top:0;left:0;width:1200px;height:44px;background:var(--grey-light)}
.topbar .social{position:absolute;left:64px;top:12px;display:flex;gap:14px}
.topbar .social span{width:20px;height:20px;border-radius:50%;border:1px solid #bbb;background:var(--white)}
.topbar .call{position:absolute;right:64px;top:13px;font-size:15px}
.topbar .call b{font-weight:700}

/* header */
.header{top:44px;left:0;width:1200px;height:89px;background:var(--white)}
.brand{position:absolute;left:64px;top:18px;display:flex;align-items:center;gap:14px}
.brand-mark{width:44px;height:44px;background:var(--blue-dark)}
.brand-name{font-family:'Cinzel',serif;font-weight:400;font-size:21px;line-height:26px;color:var(--blue-dark);width:360px}
.nav{position:absolute;left:553px;top:38px;display:flex;gap:0}
.nav a{font-family:'Cinzel',serif;font-size:14.5px;color:var(--ink);text-decoration:none;letter-spacing:.3px;margin-right:34px}
.nav a.active{color:var(--blue);border-bottom:2px solid var(--blue);padding-bottom:4px}

/* hero */
.hero{top:133px;left:0;width:1200px;height:543px;background:linear-gradient(90deg,#5b5b5b 0%,#8a8a8a 25%,#6f6f6f 55%,#4e4e4e 100%)}
.hero-copy{position:absolute;right:62px;top:164px;text-align:right;font-family:'Cinzel',serif;font-size:36px;line-height:43px;color:var(--white)}
.hero-cta{position:absolute;left:930px;top:448px;width:210px;height:58px;background:var(--black);border-radius:6px;color:var(--white);font-size:22px;display:flex;align-items:center;padding-left:18px}
.hero-cta .dot{position:absolute;right:0;top:0;width:58px;height:58px;border-radius:50%;background:var(--blue);display:flex;align-items:center;justify-content:center}
.slide-arrow{position:absolute;top:388px;width:42px;height:34px;background:#222;display:flex;align-items:center;justify-content:center}
.slide-arrow.prev{left:0}.slide-arrow.next{right:0}

/* welcome */
.welcome{top:676px;left:0;width:1200px;height:329px;text-align:center}
.section-title{font-family:'Cinzel',serif;font-weight:600;font-size:29px;color:var(--black)}
.section-title em{font-style:normal;color:var(--blue)}
.welcome .section-title{position:absolute;top:38px;left:0;width:1200px}
.welcome .rule{position:absolute;top:82px;left:118px;width:966px;height:2px;background:var(--black)}
.welcome p{position:absolute;top:112px;left:68px;width:1064px;font-size:13.5px;line-height:23px}
.btn-more{position:absolute;top:234px;left:540px;height:34px;display:flex;border-radius:4px;overflow:hidden}
.btn-more span{background:var(--black);color:var(--white);font-size:13px;padding:0 14px;line-height:34px}
.btn-more i{width:28px;background:var(--blue);display:flex;align-items:center;justify-content:center}

/* services */
.services{top:1005px;left:0;width:1200px;height:1116px}
.services .half-left{position:absolute;left:0;top:0;width:600px;height:1116px;background:var(--blue)}
.services .half-right{position:absolute;left:600px;top:0;width:600px;height:1116px;background:var(--black)}
.services .tab{position:absolute;left:420px;top:0;width:364px;height:56px}
.services .tab-label{position:absolute;left:420px;top:8px;width:364px;text-align:center;font-family:'Cinzel',serif;font-weight:600;font-size:29px}
.services .tab-label em{font-style:normal;color:var(--blue)}
.svc-col{position:absolute;top:100px;width:560px}
.svc-col.left{left:62px}.svc-col.right{left:626px}
.svc{height:142px;display:flex;align-items:flex-start}
.svc .icon{width:120px;flex:none;height:120px;position:relative}
.svc .diamond{position:absolute;left:23px;top:23px;width:74px;height:74px;background:var(--white);transform:rotate(45deg);outline:2px solid var(--white);outline-offset:5px}
.svc.on-dark .diamond{outline-color:var(--white)}
.svc .icon svg{position:absolute;left:38px;top:38px;width:44px;height:44px}
.svc .text{padding-left:12px;padding-top:2px}
.svc h3{font-weight:400;font-size:19px;line-height:24px;margin-bottom:6px}
.svc p{font-size:13.5px;line-height:19px;width:380px}
.left .svc h3,.left .svc p{color:var(--black)}
.left .svc p{color:var(--white)}
.right .svc h3{color:var(--blue)}
.right .svc p{color:var(--white)}

/* news */
.news{top:2121px;left:0;width:1200px;height:531px}
.news .section-title{position:absolute;top:40px;left:0;width:1200px;text-align:center}
.news .rule{position:absolute;top:84px;left:420px;width:364px;height:2px;background:var(--black)}
.card{position:absolute;top:118px;width:344px}
.card .media{width:344px;height:187px;position:relative}
.card .date{position:absolute;left:9px;top:9px;width:53px;height:103px;background:var(--blue);color:var(--white);font-size:15px;line-height:22px;padding:6px 0 0 10px}
.card h4{margin-top:38px;font-size:17px;font-weight:700;color:var(--black)}
.card p{margin-top:10px;font-size:13.5px;line-height:19px;color:var(--ink);width:320px}
.card .meta{margin-top:18px;border-top:2px solid var(--line);padding-top:12px;font-size:12.5px;display:flex;gap:18px}
.card .meta b{font-weight:700}
.card .meta .sep{border-left:1px solid var(--line);padding-left:18px}

/* newsletter */
.newsletter{top:2652px;left:0;width:1200px;height:96px;background:var(--grey-mid)}
.newsletter .env{position:absolute;left:60px;top:26px;width:46px;height:46px;border-radius:50%;background:var(--blue);display:flex;align-items:center;justify-content:center}
.newsletter .label{position:absolute;left:128px;top:30px;font-family:'Cinzel',serif;font-size:28px;color:var(--white);letter-spacing:1px}
.newsletter .chev{position:absolute;left:434px;top:20px}
.newsletter .field{position:absolute;left:494px;top:26px;width:461px;height:44px;background:var(--white);font-size:14px;padding:13px 12px;color:var(--ink)}
.newsletter .btn{position:absolute;left:981px;top:26px;width:157px;height:44px;background:var(--blue);color:var(--white);font-size:20px;font-weight:700;text-align:center;line-height:44px}

/* contact */
.contact{top:2748px;left:0;width:1200px;height:430px}
.map{position:absolute;left:0;top:0;width:447px;height:430px;background:linear-gradient(135deg,#dcdcdc,#c4c4c4)}
.touch{position:absolute;left:447px;top:0;width:369px;height:430px;background:#3b3b3b}
.inquiry{position:absolute;left:816px;top:0;width:384px;height:430px;background:#222}
.contact h2{position:absolute;top:42px;font-weight:400;font-size:31px;color:var(--white)}
.touch h2{left:30px}.inquiry h2{left:49px}
.info{position:absolute;left:30px;display:flex;gap:20px;color:var(--white);font-size:14px;line-height:20px}
.info .ic{width:30px;height:30px;background:var(--blue);flex:none;display:flex;align-items:center;justify-content:center}
.inq-field{position:absolute;left:49px;width:273px;background:var(--white);font-size:14px;padding:11px 10px;color:var(--ink)}
.inq-btn{position:absolute;left:49px;top:318px;width:151px;height:36px;background:var(--blue);color:var(--white);font-size:19px;font-weight:700;text-align:center;line-height:36px}

/* footer */
.footer{top:3178px;left:0;width:1200px;height:42px;background:var(--black)}
.footer .copy{position:absolute;left:60px;top:13px;font-size:13px;color:var(--white)}
.footer .social{position:absolute;right:60px;top:11px;display:flex;gap:22px}
.footer .social span{width:20px;height:20px;border-radius:50%;background:var(--white)}
</style>
</head>
<body>

<div class="abs topbar">
  <div class="social"><span></span><span></span><span></span><span></span></div>
  <div class="call">Call Us: <b>(212) 555-0148</b></div>
</div>

<header class="abs header">
  <div class="brand">
    <div class="brand-mark"></div>
    <div class="brand-name">Law Offices of Tobias R. Venkland, PLLC</div>
  </div>
  <nav class="nav">
    <a class="active">Home</a><a>Practice Areas</a><a>Privacy Policy</a><a>News</a><a>Contact Us</a>
  </nav>
</header>

<section class="abs hero" role="img" aria-label="Photograph of the attorney in a suit standing before stone columns of a courthouse">
  <div class="hero-copy">We Care About Our Clients<br>&amp; Believe In Cultivating<br>Long-term Relationships</div>
  <div class="hero-cta">Call Us Today
    <span class="dot"><svg width="22" height="16" viewBox="0 0 22 16"><path d="M2 2l6 6-6 6M11 2l6 6-6 6" stroke="#fff" stroke-width="2.5" fill="none"/></svg></span>
  </div>
  <div class="slide-arrow prev"><svg width="12" height="16" viewBox="0 0 12 16"><path d="M10 1L3 8l7 7" stroke="#fff" stroke-width="2.5" fill="none"/></svg></div>
  <div class="slide-arrow next"><svg width="12" height="16" viewBox="0 0 12 16"><path d="M2 1l7 7-7 7" stroke="#fff" stroke-width="2.5" fill="none"/></svg></div>
</section>

<section class="abs welcome">
  <h1 class="section-title">Welcome to <em>Law Offices of Tobias R. Venkland, PLLC</em></h1>
  <div class="rule"></div>
  <p>Lorem ipsum dolor sit amet, consectetuer adipiscing elit, sed diam nonummy nibh euismod tincidunt ut laoreet dolore magna aliquam erat volutpat. Ut wisi enim ad minim veniam, quis nostrud exerci tation ullamcorper suscipit lobortis nisl ut aliquip ex ea commodo consequat. Duis autem vel eum iriure dolor in hendrerit in vulputate velit esse molestie consequat, vel illum dolore eu feugiat nulla facilisis at vero eros et accumsan et iusto odio dignissim qui blandit praesent luptatum zzril delenit augue duis dolore te feugait nulla facilisi.</p>
  <div class="btn-more"><span>Read More</span><i><svg width="14" height="12" viewBox="0 0 14 12"><path d="M1 1l5 5-5 5M7 1l5 5-5 5" stroke="#fff" stroke-width="2" fill="none"/></svg></i></div>
</section>

<section class="abs services">
  <div class="half-left"></div>
  <div class="half-right"></div>
  <svg class="tab" viewBox="0 0 364 56" preserveAspectRatio="none"><path d="M0 56 C20 56 25 0 50 0 H314 C339 0 344 56 364 56 Z" fill="#fff"/></svg>
  <h2 class="tab-label">Our <em>Services</em></h2>

  <div class="svc-col left">
    <div class="svc"><div class="icon"><div class="diamond"></div><svg viewBox="0 0 44 44" fill="#3b82c4"><path d="M22 4L4 14h36z"/><rect x="8" y="17" width="4" height="16"/><rect x="16" y="17" width="4" height="16"/><rect x="24" y="17" width="4" height="16"/><rect x="32" y="17" width="4" height="16"/><rect x="4" y="35" width="36" height="4"/></svg></div>
      <div class="text"><h3>Estate Planning</h3><p>Lorem ipsum dolor sit amet, consectetuer adipiscing elit, sed diam nonummy nibh euismod tincidunt ut laoreet dolore magna aliquam erat volutpat.</p></div></div>
    <div class="svc"><div class="icon"><div class="diamond"></div><svg viewBox="0 0 44 44" fill="none" stroke="#3b82c4" stroke-width="3"><rect x="9" y="5" width="24" height="32"/><path d="M14 13h14M14 19h14M14 25h9M26 34l12-12"/></svg></div>
      <div class="text"><h3>Wills</h3><p>Lorem ipsum dolor sit amet, consectetuer adipiscing elit, sed diam nonummy nibh euismod tincidunt ut laoreet dolore magna aliquam erat volutpat.</p></div></div>
    <div class="svc"><div class="icon"><div class="diamond"></div><svg viewBox="0 0 44 44" fill="none" stroke="#3b82c4" stroke-width="3"><path d="M3 18l10-6 9 5 9-5 10 6M8 22l10 10 4-3 4 3 10-10"/></svg></div>
      <div class="text"><h3>Trusts</h3><p>Lorem ipsum dolor sit amet, consectetuer adipiscing elit, sed diam nonummy nibh euismod tincidunt ut laoreet dolore magna aliquam erat volutpat.</p></div></div>
    <div class="svc"><div class="icon"><div class="diamond"></div><svg viewBox="0 0 44 44" fill="none" stroke="#3b82c4" stroke-width="3.5"><circle cx="22" cy="7" r="3.5" fill="#3b82c4"/><path d="M20 13v12h11l4 10M16 20a10 10 0 1 0 12 14"/></svg></div>
      <div class="text"><h3>Planning For People With Disabilities</h3><p>Lorem ipsum dolor sit amet, consectetuer adipiscing elit, sed diam nonummy nibh euismod tincidunt ut laoreet dolore magna aliquam erat volutpat.</p></div></div>
    <div class="svc"><div class="icon"><div class="diamond"></div><svg viewBox="0 0 44 44"><path d="M14 20v-6a8 8 0 0 1 16 0v6" stroke="#3b82c4" stroke-width="3.5" fill="none"/><rect x="9" y="20" width="26" height="20" fill="#3b82c4"/><rect x="20" y="26" width="4" height="8" fill="#fff"/></svg></div>
      <div class="text"><h3>Asset Protection And Preservation</h3><p>Lorem ipsum dolor sit amet, consectetuer adipiscing elit, sed diam nonummy nibh euismod tincidunt ut laoreet dolore magna aliquam erat volutpat.</p></div></div>
    <div class="svc"><div class="icon"><div class="diamond"></div><svg viewBox="0 0 44 44"><rect x="16" y="6" width="12" height="6" fill="none" stroke="#3b82c4" stroke-width="3"/><rect x="5" y="12" width="34" height="26" rx="3" fill="#3b82c4"/><path d="M22 18v14M15 25h14" stroke="#fff" stroke-width="4"/></svg></div>
      <div class="text"><h3>Medicaid Planning</h3><p>Lorem ipsum dolor sit amet, consectetuer adipiscing elit, sed diam nonummy nibh euismod tincidunt ut laoreet dolore magna aliquam erat volutpat.</p></div></div>
    <div class="svc"><div class="icon"><div class="diamond"></div><svg viewBox="0 0 44 44" fill="#3b82c4"><rect x="4" y="4" width="20" height="36"/><rect x="26" y="18" width="14" height="22"/><path d="M14 10v12M8 16h12" stroke="#fff" stroke-width="3"/></svg></div>
      <div class="text"><h3>Hospital Safe Discharge</h3><p>Lorem ipsum dolor sit amet, consectetuer adipiscing elit, sed diam nonummy nibh euismod tincidunt ut laoreet dolore magna aliquam erat volutpat.</p></div></div>
  </div>

  <div class="svc-col right">
    <div class="svc on-dark"><div class="icon"><div class="diamond"></div><svg viewBox="0 0 44 44" fill="#3b82c4"><path d="M10 16a12 6 0 0 1 24 0z"/><circle cx="22" cy="24" r="7"/><path d="M8 42a14 12 0 0 1 28 0z"/></svg></div>
      <div class="text"><h3>Nursing Home Placement</h3><p>Lorem ipsum dolor sit amet, consectetuer adipiscing elit, sed diam nonummy nibh euismod tincidunt ut laoreet dolore magna aliquam erat volutpat.</p></div></div>
    <div class="svc on-dark"><div class="icon"><div class="diamond"></div><svg viewBox="0 0 44 44" fill="none" stroke="#3b82c4" stroke-width="3"><path d="M10 4h17l8 8v28H10z"/><path d="M15 18h15M15 24h15M15 30h15"/></svg></div>
      <div class="text"><h3>Powers Of Attorney</h3><p>Lorem ipsum dolor sit amet, consectetuer adipiscing elit, sed diam nonummy nibh euismod tincidunt ut laoreet dolore magna aliquam erat volutpat.</p></div></div>
    <div class="svc on-dark"><div class="icon"><div class="diamond"></div><svg viewBox="0 0 44 44" fill="#3b82c4"><circle cx="14" cy="8" r="4"/><circle cx="30" cy="10" r="4"/><rect x="10" y="14" width="8" height="16"/><rect x="26" y="16" width="8" height="14"/><path d="M11 30h3v10h-3zM27 30h3v10h-3z"/></svg></div>
      <div class="text"><h3>Health Care Proxies</h3><p>Lorem ipsum dolor sit amet, consectetuer adipiscing elit, sed diam nonummy nibh euismod tincidunt ut laoreet dolore magna aliquam erat volutpat.</p></div></div>
    <div class="svc on-dark"><div class="icon"><div class="diamond"></div><svg viewBox="0 0 44 44" fill="none" stroke="#3b82c4" stroke-width="3"><rect x="6" y="6" width="32" height="32"/><path d="M12 14h20M12 20h20M12 26h20M12 32h12"/></svg></div>
      <div class="text"><h3>Living Wills</h3><p>Lorem ipsum dolor sit amet, consectetuer adipiscing elit, sed diam nonummy nibh euismod tincidunt ut laoreet dolore magna aliquam erat volutpat.</p></div></div>
    <div class="svc on-dark"><div class="icon"><div class="diamond"></div><svg viewBox="0 0 44 44" fill="none" stroke="#3b82c4" stroke-width="2.5"><path d="M22 4v34M8 10h28M14 40h16"/><path d="M8 10l-5 12h10zM36 10l-5 12h10z"/></svg></div>
      <div class="text"><h3>Guardianships</h3><p>Lorem ipsum dolor sit amet, consectetuer adipiscing elit, sed diam nonummy nibh euismod tincidunt ut laoreet dolore magna aliquam erat volutpat.</p></div></div>
    <div class="svc on-dark"><div class="icon"><div class="diamond"></div><svg viewBox="0 0 44 44" fill="#3b82c4"><path d="M8 8h22l6 6v22H14l-6-6z"/><path d="M14 16h14M14 22h14M14 28h10" stroke="#fff" stroke-width="2.5"/></svg></div>
      <div class="text"><h3>Probate</h3><p>Lorem ipsum dolor sit amet, consectetuer adipiscing elit, sed diam nonummy nibh euismod tincidunt ut laoreet dolore magna aliquam erat volutpat.</p></div></div>
    <div class="svc on-dark"><div class="icon"><div class="diamond"></div><svg viewBox="0 0 44 44" fill="none" stroke="#3b82c4" stroke-width="3"><rect x="4" y="8" width="36" height="22"/><path d="M16 38h12M22 30v8M12 22l8-7 6 4 8-7"/></svg></div>
      <div class="text"><h3>Estate Administration &amp; Related Litigation</h3><p>Lorem ipsum dolor sit amet, consectetuer adipiscing elit, sed diam nonummy nibh euismod tincidunt ut laoreet dolore magna aliquam erat volutpat.</p></div></div>
  </div>
</section>

<section class="abs news">
  <h2 class="section-title">Latest <em>News</em></h2>
  <div class="rule"></div>

  <article class="card" style="left:60px">
    <div class="media" role="img" aria-label="Photograph of an older couple reviewing documents with an adviser" style="background:linear-gradient(135deg,#b89a7c,#e4d7c6 60%,#cfc3b3)"><div class="date">12<br>July<br>2016</div></div>
    <h4>Lorem Ipsum Dolor</h4>
    <p>Sed ut perspiciatis unde omnis iste natus errorluptatem accusa nt ium dolorem que laudantium totam rem aperiam laudantium</p>
    <div class="meta"><span><b>By :</b> Sed ut perspiciatis</span><span class="sep"><b>0</b> Comments</span></div>
  </article>

  <article class="card" style="left:429px">
    <div class="media" role="img" aria-label="Photograph of a judge's gavel beside a hand signing papers" style="background:linear-gradient(135deg,#2a1a14,#6b3a24 55%,#d8d2cc)"><div class="date">12<br>July<br>2016</div></div>
    <h4>Lorem Ipsum Dolor</h4>
    <p>Sed ut perspiciatis unde omnis iste natus errorluptatem accusa nt ium dolorem que laudantium totam rem aperiam laudantium</p>
    <div class="meta"><span><b>By :</b> Sed ut perspiciatis</span><span class="sep"><b>0</b> Comments</span></div>
  </article>

  <article class="card" style="left:794px">
    <div class="media" role="img" aria-label="Photograph of a pen resting on a last will and testament document" style="background:linear-gradient(135deg,#f3f1ec,#d9dde4 60%,#6f86b3)"><div class="date">12<br>July<br>2016</div></div>
    <h4>Lorem Ipsum Dolor</h4>
    <p>Sed ut perspiciatis unde omnis iste natus errorluptatem accusa nt ium dolorem que laudantium totam rem aperiam laudantium</p>
    <div class="meta"><span><b>By :</b> Sed ut perspiciatis</span><span class="sep"><b>0</b> Comments</span></div>
  </article>
</section>

<section class="abs newsletter">
  <div class="env"><svg width="24" height="18" viewBox="0 0 24 18"><rect x="1" y="1" width="22" height="16" fill="none" stroke="#fff" stroke-width="2"/><path d="M1 1l11 9 11-9" fill="none" stroke="#fff" stroke-width="2"/></svg></div>
  <div class="label">Newsletter Signup</div>
  <svg class="chev" width="30" height="56" viewBox="0 0 30 56"><path d="M4 2l22 26L4 54" fill="none" stroke="#fff" stroke-width="3"/></svg>
  <div class="field">Your e-mail</div>
  <div class="btn">Sign Up</div>
</section>

<section class="abs contact">
  <div class="map" role="img" aria-label="Street map of the Midtown Manhattan area with the office location pinned"></div>
  <div class="touch">
    <h2>Get In Touch</h2>
    <div class="info" style="top:110px"><span class="ic"><svg width="14" height="18" viewBox="0 0 14 18"><path d="M7 1a6 6 0 0 1 6 6c0 5-6 10-6 10S1 12 1 7a6 6 0 0 1 6-6z" fill="#fff"/><circle cx="7" cy="7" r="2" fill="#3b82c4"/></svg></span><div><b>Law Offices Of Tobias R. Venkland, PLLC</b><br>218 Harlow Avenue, Suite 1204<br>New York, New York 10118</div></div>
    <div class="info" style="top:205px"><span class="ic"><svg width="16" height="16" viewBox="0 0 16 16"><path d="M3 1l3 3-2 2c1 2 4 5 6 6l2-2 3 3-2 3C7 15 1 9 1 3z" fill="#fff"/></svg></span><div style="padding-top:5px"><b>(212) 555-0148</b></div></div>
    <div class="info" style="top:270px"><span class="ic"><svg width="16" height="16" viewBox="0 0 16 16"><rect x="4" y="1" width="8" height="5" fill="#fff"/><rect x="1" y="6" width="14" height="6" fill="#fff"/><rect x="4" y="10" width="8" height="5" fill="#fff" stroke="#3b82c4"/></svg></span><div style="padding-top:5px"><b>(212) 555-0193</b></div></div>
    <div class="info" style="top:335px"><span class="ic"><svg width="16" height="12" viewBox="0 0 16 12"><rect x="1" y="1" width="14" height="10" fill="none" stroke="#fff" stroke-width="1.5"/><path d="M1 1l7 6 7-6" fill="none" stroke="#fff" stroke-width="1.5"/></svg></span><div style="padding-top:5px">info@venklandlaw.example</div></div>
  </div>
  <div class="inquiry">
    <h2>Quick Inquiry</h2>
    <div class="inq-field" style="top:114px;height:41px">Your name</div>
    <div class="inq-field" style="top:168px;height:43px">Your e-mail</div>
    <div class="inq-field" style="top:226px;height:75px">Your message</div>
    <div class="inq-btn">Submit</div>
  </div>
</section>

<footer class="abs footer">
  <div class="copy">Copyright © 2016 Law Offices Of Tobias R. Venkland, Pllc. All Right Reserved.</div>
  <div class="social"><span></span><span></span><span></span><span></span></div>
</footer>

</body>
</html>
```